Business card design for global fintech startup

Veltrix is a modern payments platform for the global insurance industry, serving international health, life, and travel insurers, MGAs, brokers, and partners.

We need a professional, premium business card for use at insurance conferences and executive meetings. The goal is to create a card that feels trustworthy, modern, and high-quality, while still being distinctive and memorable in a stack of business cards.

Target audience:
Senior insurance executives (VP, C-suite).

Design goals:
Clear, professional, and credible
Modern but not trendy
Premium and well-structured
Easy to read and practical for networking

Brand direction:
Brand-first (company over individual)
Follow existing brand guidelines where possible
Clean layout, strong hierarchy, excellent readability

Must include:
Name
Title
Company name (Veltrix)
Logo
Email
Phone/Whatsapp
Website (www.withveltrix.example)
Tagline - Clarity in every payment

Materials & finish:
Open to designer recommendations for premium look and feel.

Please avoid:
Flashy or trendy startup styles
Generic insurance icons or clichés
Cluttered layouts or hard-to-read text

Deliverables:
Front and back business card, print-ready files.

Target Market(s)

Global Insurance executives

Industry/Entity Type

Fintech, Insurtech, Insurance, Financial Services

Contact Information for Business Card

Name Title Company name (Veltrix) Logo Email Phone/Whatsapp Website (www.withveltrix.example) Tagline - Clarity in every payment

Font styles to use
Other font styles liked:
• See brand guidelines

Requirements
Nice to have
• something that stands out/makes us more memorable while still remaining professional
Should not have
• Please avoid: Flashy or trendy startup styles Generic insurance icons or clichés Cluttered layouts or hard-to-read text

```html
<!DOCTYPE html>
<html lang="en">
<head>
<meta charset="utf-8">
<title>Veltrix business card</title>
<link href="https://fonts.googleapis.com/css2?family=Montserrat:wght@400;600&family=Open+Sans:wght@400;600&family=Questrial&display=swap" rel="stylesheet">
<style>
  :root {
    --page-bg: #f6f6f6;
    --card-white: #ffffff;
    --card-black: #0b0b0b;
    --ink: #1f1f24;
    --navy-rule: #2c3550;
    --brand-blue: #4a8fd0;
    --accent-orange: #f07a22;
  }
  * { margin: 0; padding: 0; box-sizing: border-box; }
  html, body { width: 891px; height: 1200px; overflow: hidden; background: var(--page-bg); }
  .canvas { position: relative; width: 891px; height: 1200px; }

  .card {
    position: absolute;
    left: 168px;
    width: 556px;
    height: 315px;
    overflow: hidden;
  }
  .card--back { top: 235px; background: var(--card-black); }
  .card--front { top: 720px; background: var(--card-white); }

  /* back side */
  .back-brand {
    position: absolute; inset: 0;
    display: flex; align-items: center; justify-content: center; gap: 18px;
  }
  .back-brand__dot { width: 34px; height: 34px; border-radius: 50%; background: var(--brand-blue); }
  .back-brand__name {
    font-family: "Montserrat", sans-serif; font-weight: 400;
    font-size: 44px; letter-spacing: 8px; color: #ffffff;
  }

  /* front side */
  .name-bar {
    position: absolute; left: 0; top: 132px; width: 14px; height: 55px;
    background: var(--accent-orange);
  }
  .person-name {
    position: absolute; left: 25px; top: 138px;
    font-family: "Montserrat", sans-serif; font-weight: 600;
    font-size: 28px; line-height: 1; color: var(--brand-blue); letter-spacing: -0.3px;
  }
  .person-title {
    position: absolute; left: 31px; top: 168px;
    font-family: "Montserrat", sans-serif; font-weight: 400;
    font-size: 11px; letter-spacing: 3.2px; color: var(--ink);
  }
  .divider {
    position: absolute; left: 252px; top: 60px; width: 1px; height: 193px;
    background: var(--navy-rule);
  }
  .brand {
    position: absolute; left: 268px; top: 68px;
    display: flex; align-items: center; gap: 16px;
  }
  .brand__dot { width: 50px; height: 50px; border-radius: 50%; background: var(--brand-blue); }
  .brand__name {
    display: block;
    font-family: "Open Sans", sans-serif; font-weight: 600;
    font-size: 37px; line-height: 1; letter-spacing: 4px; color: var(--ink);
  }
  .brand__tagline {
    display: block; margin-top: 3px;
    font-family: "Open Sans", sans-serif; font-weight: 400;
    font-size: 12px; letter-spacing: 0.6px; color: var(--ink);
  }
  .contacts { position: absolute; left: 278px; top: 138px; list-style: none; }
  .contacts li {
    display: flex; align-items: center; height: 24.5px;
    font-family: "Questrial", sans-serif; font-size: 15.5px; color: var(--ink); letter-spacing: 0.5px;
  }
  .contacts svg { width: 18px; height: 18px; margin-right: 9px; flex: none; }
  .contacts .hl { color: var(--brand-blue); }
</style>
</head>
<body>
<main class="canvas">
  <section class="card card--back" aria-label="Card back">
    <div class="back-brand">
      <span class="back-brand__dot"></span>
      <span class="back-brand__name">VELTRIX</span>
    </div>
  </section>

  <section class="card card--front" aria-label="Card front">
    <div class="name-bar"></div>
    <p class="person-name">YOUR NAME</p>
    <p class="person-title">MANAGER</p>

    <div class="divider"></div>

    <div class="brand">
      <span class="brand__dot"></span>
      <div>
        <span class="brand__name">VELTRIX</span>
        <span class="brand__tagline">CLARITY IN EVERY PAYMENT</span>
      </div>
    </div>

    <ul class="contacts">
      <li>
        <svg viewBox="0 0 24 24"><path fill="#4a8fd0" d="M6.6 2.5l3 3.4-1.8 2.3c1.1 2.8 3.4 5.2 6.2 6.3l2.2-1.8 3.4 3-2 3.3C9.8 18.6 5.2 13.4 3.9 4.6z"/></svg>
        555-014-2738
      </li>
      <li>
        <svg viewBox="0 0 24 24"><rect x="6.5" y="2" width="11" height="20" rx="1.8" fill="none" stroke="#4a8fd0" stroke-width="1.8"/><line x1="6.5" y1="18" x2="17.5" y2="18" stroke="#4a8fd0" stroke-width="1.4"/></svg>
        555-014-2739
      </li>
      <li>
        <svg viewBox="0 0 24 24"><rect x="2" y="5" width="20" height="14" fill="#4a8fd0"/><path d="M2 5l10 8 10-8M2 19l7.5-7M22 19l-7.5-7" fill="none" stroke="#fff" stroke-width="1.3"/></svg>
        <span>info@<span class="hl">withveltrix</span>.example</span>
      </li>
      <li>
        <svg viewBox="0 0 24 24" fill="none" stroke="#4a8fd0" stroke-width="1.4"><circle cx="12" cy="12" r="9"/><ellipse cx="12" cy="12" rx="4" ry="9"/><line x1="3" y1="12" x2="21" y2="12"/><path d="M4.5 7.5h15M4.5 16.5h15"/></svg>
        <span>www.<span class="hl">withveltrix</span>.example</span>
      </li>
    </ul>
  </section>
</main>
</body>
</html>
```